Design us a professional website for a Cannabis Staffing Agency

We already have a logo ready to go, but now we are looking for a few good web designs. We provide staffing for the Cannabis/Marijuana industry. We want a good balance of clean, simple and modern design but also embracing the exciting atmosphere of the Cannabis industry.

Here are examples of our competition, please note that most of these competitors design feel old and dated:

http://qrvplacementcrew.example/
https://tolbrix.example/tolbrix-main-page
http://saffronpathways.example/index.html
http://www.wickcrew.example/medical-marijuana-staffing-recruiting
http://www.tundrahiring.example/
www.placedupcrew.example
www.pinewise.example

I also would prefer an explanation of why you choose to design it the way you did? What was your thought process or did you use a template?

Requirements
Must have
• About Us Page
• Candidates Page
• Employer Page
• Job Opening Page
• Contact Us Page
Nice to have
• Colors to match the logo, good use of images and design to show the story. Our goal is to show our clients what we are about and not just tell them.

```html
<!DOCTYPE html>
<html lang="en">
<head>
<meta charset="utf-8">
<title>Verdanta — Cannabis Staffing</title>
<link rel="stylesheet" href="https://fonts.googleapis.com/css2?family=Raleway:wght@400;500;600;700;800&display=swap">
<style>
:root{
  --green:#5f9a08;
  --green-dark:#4e8405;
  --green-light:#c4dd97;
  --green-pale:#d7e8b8;
  --ink:#444;
  --grey:#5b5b5b;
  --grey-dark:#3e3e3e;
  --white:#fff;
}
*{box-sizing:border-box;margin:0;padding:0}
html,body{width:1200px;height:3232px;overflow:hidden}
body{position:relative;font-family:'Raleway',sans-serif;color:var(--ink);background:var(--white)}
.abs{position:absolute}
.center{text-align:center}
.upper{text-transform:uppercase}

/* header */
.site-header{left:0;top:0;width:1200px;height:69px;background:var(--white)}
.brand{left:150px;top:14px;display:flex;align-items:center;gap:10px}
.brand-dot{width:40px;height:40px;border-radius:50%;background:var(--green)}
.brand-name{font-weight:800;font-size:26px;color:var(--green);letter-spacing:1px}
.main-nav{right:95px;top:0;display:flex;height:69px}
.main-nav a{display:flex;align-items:center;padding:0 16px;font-size:13px;color:var(--green);text-decoration:none;text-transform:uppercase}
.main-nav a.active{background:var(--green);color:var(--white)}

/* hero */
.hero{left:0;top:69px;width:1200px;height:157px;background:radial-gradient(ellipse at 60% 40%,#7ea64a 0%,#3f6a1c 55%,#2a4a14 100%)}
.hero h1{width:1200px;top:66px;font-size:34px;font-weight:800;color:var(--white);letter-spacing:1px}
.hero p{width:1200px;top:104px;font-size:18px;color:var(--white)}
.intro{left:0;top:226px;width:1200px;height:144px;background:var(--white);border-top:2px solid #e2e2e2}
.intro h2{width:1200px;top:48px;font-size:28px;font-weight:800;color:var(--green)}
.intro p{width:1200px;top:84px;font-size:11px;color:#9a9a9a;letter-spacing:.5px}
.cta-band{left:0;top:370px;width:1200px;height:147px;background:linear-gradient(90deg,#8a7f63,#c6c0ad 40%,#b5b09c 60%,#7d7a66)}
.cta-strip{left:0;top:54px;width:1200px;height:63px;background:#c9c9c3}
.btn{display:flex;align-items:center;justify-content:center;font-size:13px;font-weight:700;text-transform:uppercase;letter-spacing:.5px;text-decoration:none}
.btn-green{background:var(--green);color:var(--white);border:3px solid var(--white)}
.btn-white{background:var(--white);color:var(--green)}
.cta-badge{left:560px;top:28px;width:86px;height:86px;border-radius:50%;background:var(--green);border:4px solid var(--white);box-shadow:0 3px 8px rgba(0,0,0,.3)}

/* about */
.section-title{width:1200px;font-size:36px;font-weight:500;color:var(--green)}
.photo-circle{border-radius:50%}
.about-title{width:300px;font-size:13px;font-weight:700;color:var(--green)}
.about-text{width:260px;font-size:12.5px;line-height:18px;color:var(--ink)}
.btn-outline{border:1px solid var(--green);color:var(--green);font-weight:500}
.people-strip{left:0;top:1245px;width:1200px;height:116px;background:linear-gradient(90deg,#a8a294,#7e7a70 20%,#b4aea2 40%,#8c8676 60%,#b0aa9c 80%,#6f6a5f)}

/* info sections */
.candidates{left:0;top:1361px;width:1200px;height:552px;background:var(--green)}
.employer{left:0;top:1913px;width:1200px;height:568px;background:var(--green-light)}
.info-title{width:1200px;font-size:34px;font-weight:800;color:var(--white)}
.rule{height:2px;background:var(--white)}
.icon-ring{width:112px;height:112px}
.info-label{width:220px;font-size:13px;font-weight:800;color:var(--white);text-transform:uppercase}
.info-box{width:164px;padding:5px 6px;font-size:10px;line-height:12.4px;text-align:justify;text-align-last:center}
.candidates .info-box{border:1px solid #a9cc6d;color:var(--white)}
.employer .info-box{border:1px solid #e3efcc;color:#8fae5c}
.btn-plain{background:var(--white);color:var(--green)}

/* reviews */
.avatar{width:108px;height:108px;border-radius:50%;border:4px solid var(--green)}
.review-text{width:230px;font-size:12px;line-height:16px;color:var(--green);text-align:center}
.dots{left:573px;top:2874px;display:flex;gap:8px}
.dots span{width:7px;height:7px;border-radius:50%;background:#ccc}
.dots span:first-child{background:#999}

/* footer */
.site-footer{left:0;top:2968px;width:1200px;height:237px;background:var(--grey)}
.btn-dark{border:2px solid #8a8a8a;background:#5f5f5f;color:#3c3c3c}
.footer-brand{left:495px;top:-6px;width:147px;height:60px;background:var(--white);display:flex;align-items:center;justify-content:center;gap:6px;border-radius:0 0 6px 6px}
.footer-brand .brand-dot{width:26px;height:26px}
.footer-brand .brand-name{font-size:17px}
.footer-links{width:300px;font-size:12px;line-height:22px;color:#dcdcdc;text-transform:uppercase}
.social{width:38px;height:38px;border-radius:50%;border:2px solid var(--white)}
.contact{width:300px;left:450px;font-size:12px;line-height:19px;color:#eee}
.copyright{left:0;top:3205px;width:1200px;height:27px;background:var(--green);color:var(--white);font-size:11px;display:flex;align-items:center;justify-content:center}
</style>
</head>
<body>

<header class="abs site-header">
  <div class="abs brand"><span class="brand-dot"></span><span class="brand-name">VERDANTA</span></div>
  <nav class="abs main-nav">
    <a href="#">Home</a><a href="#">About us</a><a href="#">Candidates</a><a href="#">Employer</a><a href="#">Jobs</a><a href="#" class="active">Contact us</a>
  </nav>
</header>

<section class="abs hero" role="img" aria-label="Blurred photo of green cannabis leaves">
  <h1 class="abs center upper">Lorem ipsum dolor sit amet</h1>
  <p class="abs center">sed do eiusmod tempor incididunt ut labore et dolore magna aliqua</p>
</section>

<section class="abs intro">
  <h2 class="abs center upper">Connecting cannabis companies with quality stuff</h2>
  <p class="abs center upper">Lorem ipsum dolor sit amet, consectetur adipiscing elit, sed do eiusmod tempor incididunt ut labore et dolore magna aliqua.</p>
</section>

<section class="abs cta-band" role="img" aria-label="Photo of hands holding a cannabis plant">
  <div class="abs cta-strip"></div>
  <a class="abs btn btn-green" style="left:243px;top:61px;width:263px;height:51px">Register candidate</a>
  <div class="abs cta-badge"></div>
  <a class="abs btn btn-white" style="left:694px;top:61px;width:260px;height:51px">Register business</a>
</section>

<section class="about">
  <h2 class="abs section-title center upper" style="top:562px">About us</h2>
  <div class="abs photo-circle" style="left:185px;top:743px;width:224px;height:224px;background:radial-gradient(circle,#8fb46a,#3f6b2a)" role="img" aria-label="Photo of a scientist examining cannabis plants"></div>
  <div class="abs photo-circle" style="left:491px;top:668px;width:224px;height:224px;background:radial-gradient(circle,#c9a98e,#6f5a4a)" role="img" aria-label="Photo of a smiling team at work"></div>
  <div class="abs photo-circle" style="left:788px;top:743px;width:224px;height:224px;background:radial-gradient(circle,#c7bfb8,#7a3038)" role="img" aria-label="Photo of two colleagues in business dress"></div>

  <h3 class="abs about-title center upper" style="left:147px;top:986px">Information number one</h3>
  <p class="abs about-text" style="left:173px;top:1015px;text-align:justify">Lorem ipsum dolor sit amet, consectetur adipiscing elit, sed do eiusmod tempor incididunt ut labore et dolore magna aliqua. Ut enim ad minim veniam, quis nostrud exercitation ullamco laboris nisi ut aliquip ex ea commodo consequat. Duis aute irure dolor in reprehenderit in voluptate velit esse cillum dolore eu fugiat nulla pariatur.</p>

  <h3 class="abs about-title center upper" style="left:453px;top:911px">Information number two</h3>
  <p class="abs about-text" style="left:473px;top:940px;text-align:center">Excepteur sint occaecat cupidatat non proident, sunt in culpa qui officia deserunt mollit anim id est laborum. Sed ut perspiciatis unde omnis iste natus error sit voluptatem accusantium doloremque laudantium, totam rem aperiam, eaque ipsa quae ab illo inventore veritatis et quasi archi.</p>

  <h3 class="abs about-title center upper" style="left:750px;top:986px">Information number three</h3>
  <p class="abs about-text" style="left:774px;top:1015px;text-align:justify">Lorem ipsum dolor sit amet, consectetur adipiscing elit, sed do eiusmod tempor incididunt ut labore et dolore magna aliqua. Ut enim ad minim veniam, quis nostrud exercitation ullamco laboris nisi ut aliquip ex ea commodo consequat. Duis aute irure dolor in reprehenderit in voluptate velit esse cillum dolore eu fugiat nulla pariatur.</p>

  <a class="abs btn btn-outline" style="left:470px;top:1146px;width:262px;height:52px">See more</a>
</section>

<div class="abs people-strip" role="img" aria-label="Photo strip of young professionals working together"></div>

<section class="abs candidates">
  <div class="abs rule" style="left:0;top:43px;width:250px"></div>
  <h2 class="abs info-title center upper" style="top:22px">Info title for new candidates</h2>
  <div class="abs rule" style="left:945px;top:43px;width:255px"></div>

  <svg class="abs icon-ring" style="left:181px;top:99px" viewBox="0 0 112 112" fill="none" stroke="#fff" stroke-width="3"><circle cx="56" cy="56" r="53"/><circle cx="56" cy="56" r="44" fill="#fff" fill-opacity=".12"/><circle cx="56" cy="42" r="16" fill="#fff" stroke="none"/><circle cx="44" cy="52" r="10" fill="#fff" stroke="none"/><circle cx="68" cy="52" r="10" fill="#fff" stroke="none"/><rect x="53" y="55" width="6" height="26" fill="#fff" stroke="none"/><line x1="40" y1="82" x2="72" y2="82"/></svg>
  <svg class="abs icon-ring" style="left:424px;top:99px" viewBox="0 0 112 112" fill="none" stroke="#fff" stroke-width="3"><circle cx="56" cy="56" r="53"/><circle cx="56" cy="56" r="44" fill="#fff" fill-opacity=".12"/><circle cx="56" cy="56" r="30"/><circle cx="56" cy="40" r="4" fill="#fff" stroke="none"/><rect x="52" y="49" width="8" height="24" fill="#fff" stroke="none"/></svg>
  <svg class="abs icon-ring" style="left:668px;top:99px" viewBox="0 0 112 112" fill="none" stroke="#fff" stroke-width="3"><circle cx="56" cy="56" r="53"/><circle cx="56" cy="56" r="44" fill="#fff" fill-opacity=".12"/><ellipse cx="56" cy="40" rx="13" ry="15" fill="#fff" stroke="none"/><path d="M30 84 Q32 60 56 60 Q80 60 82 84 Z" fill="#fff" stroke="none"/></svg>
  <svg class="abs icon-ring" style="left:915px;top:99px" viewBox="0 0 112 112" fill="none" stroke="#fff" stroke-width="3"><circle cx="56" cy="56" r="53"/><circle cx="56" cy="56" r="44" fill="#fff" fill-opacity=".12"/><rect x="36" y="28" width="40" height="56" fill="#fff" stroke="none"/><g stroke="#5f9a08" stroke-width="3"><line x1="42" y1="38" x2="70" y2="38"/><line x1="42" y1="47" x2="70" y2="47"/><line x1="42" y1="56" x2="70" y2="56"/><line x1="42" y1="65" x2="70" y2="65"/><line x1="42" y1="74" x2="70" y2="74"/></g></svg>

  <div class="abs info-label center" style="left:127px;top:229px">Consectetur adipiscing</div>
  <div class="abs info-label center" style="left:370px;top:229px">Suspendisse vitae</div>
  <div class="abs info-label center" style="left:614px;top:229px">Nulla congue</div>
  <div class="abs info-label center" style="left:861px;top:229px">Donec sed mattis adipiscing</div>

  <p class="abs info-box" style="left:155px;top:257px">Lorem ipsum dolor sit amet, consectetur adipiscing elit. Suspendisse et enim urna. Suspendisse vitae mauris sed urna vehicula porta et vel libero. Morbi lacinia risus vel libero elementum hendrerit. Mauris nunc dui, varius id mattis at, venenatis sit amet risus. Duis dapibus elit nec euismod gravida. Vivamus scelerisque eros iaculis dui semper, a imperdiet mi hendrerit. Vivamus facilisis lectus et velit ullamcorper.</p>
  <p class="abs info-box" style="left:398px;top:257px">Lorem ipsum dolor sit amet, consectetur adipiscing elit. Suspendisse et enim urna. Suspendisse vitae mauris sed urna vehicula porta et vel libero. Morbi lacinia risus vel libero elementum hendrerit. Mauris nunc dui, varius id mattis at, venenatis sit amet risus. Duis dapibus elit nec euismod gravida. Vivamus scelerisque eros iaculis dui semper, a imperdiet mi hendrerit. Vivamus facilisis lectus et velit ullamcorper.</p>
  <p class="abs info-box" style="left:642px;top:257px">Lorem ipsum dolor sit amet, consectetur adipiscing elit. Suspendisse et enim urna. Suspendisse vitae mauris sed urna vehicula porta et vel libero. Morbi lacinia risus vel libero elementum hendrerit. Mauris nunc dui, varius id mattis at, venenatis sit amet risus. Duis dapibus elit nec euismod gravida. Vivamus scelerisque eros iaculis dui semper, a imperdiet mi hendrerit. Vivamus facilisis lectus et velit ullamcorper.</p>
  <p class="abs info-box" style="left:889px;top:257px">Lorem ipsum dolor sit amet, consectetur adipiscing elit. Suspendisse et enim urna. Suspendisse vitae mauris sed urna vehicula porta et vel libero. Morbi lacinia risus vel libero elementum hendrerit. Mauris nunc dui, varius id mattis at, venenatis sit amet risus. Duis dapibus elit nec euismod gravida. Vivamus scelerisque eros iaculis dui semper, a imperdiet mi hendrerit. Vivamus facilisis lectus et velit ullamcorper.</p>

  <a class="abs btn btn-plain" style="left:506px;top:478px;width:188px;height:39px">Begin career</a>
</section>

<section class="abs employer">
  <div class="abs rule" style="left:0;top:60px;width:262px"></div>
  <h2 class="abs info-title center upper" style="top:38px">Info title for new employer</h2>
  <div class="abs rule" style="left:940px;top:60px;width:260px"></div>

  <svg class="abs icon-ring" style="left:181px;top:116px" viewBox="0 0 112 112" fill="none" stroke="#fff" stroke-width="3"><circle cx="56" cy="56" r="53"/><circle cx="56" cy="56" r="44" fill="#fff" fill-opacity=".15"/><rect x="30" y="40" width="52" height="36" rx="3" fill="#5f9a08" stroke="none"/><rect x="46" y="32" width="20" height="10" rx="2" stroke="#5f9a08"/><line x1="30" y1="56" x2="82" y2="56" stroke="#c4dd97"/></svg>
  <svg class="abs icon-ring" style="left:424px;top:116px" viewBox="0 0 112 112" fill="none" stroke="#fff" stroke-width="3"><circle cx="56" cy="56" r="53"/><circle cx="56" cy="56" r="44" fill="#fff" fill-opacity=".15"/><path d="M24 56 Q56 28 88 56 Q56 84 24 56 Z" stroke="#5f9a08" stroke-width="5"/><circle cx="56" cy="56" r="10" fill="#5f9a08" stroke="none"/></svg>
  <svg class="abs icon-ring" style="left:668px;top:116px" viewBox="0 0 112 112" fill="none" stroke="#fff" stroke-width="3"><circle cx="56" cy="56" r="53"/><circle cx="56" cy="56" r="44" fill="#fff" fill-opacity=".15"/><g stroke="#5f9a08" stroke-width="4"><circle cx="54" cy="58" r="24"/><circle cx="54" cy="58" r="14"/><line x1="54" y1="58" x2="80" y2="32"/></g><circle cx="54" cy="58" r="5" fill="#5f9a08" stroke="none"/></svg>
  <svg class="abs icon-ring" style="left:915px;top:116px" viewBox="0 0 112 112" fill="none" stroke="#fff" stroke-width="3"><circle cx="56" cy="56" r="53"/><circle cx="56" cy="56" r="44" fill="#fff" fill-opacity=".15"/><path d="M32 56 L50 74 L82 40" stroke="#5f9a08" stroke-width="11" stroke-linecap="square"/></svg>

  <div class="abs info-label center" style="left:127px;top:246px">Consectetur adipiscing</div>
  <div class="abs info-label center" style="left:370px;top:246px">Suspendisse vitae</div>
  <div class="abs info-label center" style="left:614px;top:246px">Nulla congue</div>
  <div class="abs info-label center" style="left:861px;top:246px">Donec sed mattis adipiscing</div>

  <p class="abs info-box" style="left:155px;top:273px">Lorem ipsum dolor sit amet, consectetur adipiscing elit. Suspendisse et enim urna. Suspendisse vitae mauris sed urna vehicula porta et vel libero. Morbi lacinia risus vel libero elementum hendrerit. Mauris nunc dui, varius id mattis at, venenatis sit amet risus. Duis dapibus elit nec euismod gravida. Vivamus scelerisque eros iaculis dui semper, a imperdiet mi hendrerit. Vivamus facilisis lectus et velit ullamcorper.</p>
  <p class="abs info-box" style="left:398px;top:273px">Lorem ipsum dolor sit amet, consectetur adipiscing elit. Suspendisse et enim urna. Suspendisse vitae mauris sed urna vehicula porta et vel libero. Morbi lacinia risus vel libero elementum hendrerit. Mauris nunc dui, varius id mattis at, venenatis sit amet risus. Duis dapibus elit nec euismod gravida. Vivamus scelerisque eros iaculis dui semper, a imperdiet mi hendrerit. Vivamus facilisis lectus et velit ullamcorper.</p>
  <p class="abs info-box" style="left:642px;top:273px">Lorem ipsum dolor sit amet, consectetur adipiscing elit. Suspendisse et enim urna. Suspendisse vitae mauris sed urna vehicula porta et vel libero. Morbi lacinia risus vel libero elementum hendrerit. Mauris nunc dui, varius id mattis at, venenatis sit amet risus. Duis dapibus elit nec euismod gravida. Vivamus scelerisque eros iaculis dui semper, a imperdiet mi hendrerit. Vivamus facilisis lectus et velit ullamcorper.</p>
  <p class="abs info-box" style="left:889px;top:273px">Lorem ipsum dolor sit amet, consectetur adipiscing elit. Suspendisse et enim urna. Suspendisse vitae mauris sed urna vehicula porta et vel libero. Morbi lacinia risus vel libero elementum hendrerit. Mauris nunc dui, varius id mattis at, venenatis sit amet risus. Duis dapibus elit nec euismod gravida. Vivamus scelerisque eros iaculis dui semper, a imperdiet mi hendrerit. Vivamus facilisis lectus et velit ullamcorper.</p>

  <a class="abs btn btn-plain" style="left:506px;top:495px;width:188px;height:39px">Register acrivity</a>
</section>

<svg class="abs" style="left:0;top:1895px" width="1200" height="70" viewBox="0 0 1200 70"><polygon points="0,0 1200,0 1200,62 0,12" fill="#5f9a08"/></svg>

<section class="reviews">
  <h2 class="abs section-title center upper" style="top:2550px;font-weight:700">Reviews</h2>
  <svg class="abs" style="left:152px;top:2700px" width="24" height="40" viewBox="0 0 24 40"><path d="M20 3 L5 20 L20 37" fill="none" stroke="#5f9a08" stroke-width="5"/></svg>
  <svg class="abs" style="left:1022px;top:2700px" width="24" height="40" viewBox="0 0 24 40"><path d="M4 3 L19 20 L4 37" fill="none" stroke="#5f9a08" stroke-width="5"/></svg>

  <div class="abs avatar" style="left:250px;top:2619px;background:#cfc7bd" role="img" aria-label="Portrait photo of a male client"></div>
  <div class="abs avatar" style="left:545px;top:2619px;background:#b59a86" role="img" aria-label="Portrait photo of a female client"></div>
  <div class="abs avatar" style="left:851px;top:2619px;background:#a38a72" role="img" aria-label="Portrait photo of a bearded client"></div>

  <p class="abs review-text" style="left:189px;top:2745px">Ut enim ad minim veniam, quis nostrud exercitation ullamco laboris nisi ut aliquip exea commodo consequat. Duis aute irure dolor in reprehenderit in voluptate velit esse cillum dolore eu fugiat nulla pariatur. Excepteur sint occaecat</p>
  <p class="abs review-text" style="left:484px;top:2745px">Sunt in culpa qui officia deserunt mollit animid estlaborum. Sed ut perspiciatis unde omnis iste natus error sit voluptatem accusantium doloremque laudantium, totam rem aperiam, eaque ipsa quae ab illo inventoreveritatis et quasi architecto beatae.</p>
  <p class="abs review-text" style="left:790px;top:2745px">Nemo enim ipsam voluptatem quia voluptas sit aspernatur aut odit aut fugit, sed quia consequuntur magni dolores eos qui ratione voluptatem sequi nesciunt. Neque porro quisquam est, qui dolorem ipsum quia dolor sit amet, consectetur adipisci</p>

  <div class="abs dots"><span></span><span></span><span></span><span></span></div>
</section>

<footer class="abs site-footer">
  <a class="abs btn btn-green" style="left:205px;top:18px;width:262px;height:51px;border-color:#8fc04a">Register candidate</a>
  <div class="abs footer-brand"><span class="brand-dot"></span><span class="brand-name">VERDANTA</span></div>
  <a class="abs btn btn-dark" style="left:732px;top:18px;width:263px;height:51px">Register business</a>

  <div class="abs footer-links center" style="left:186px;top:88px">In search for job?<br>Career fairs<br>FAQ<br>Contact us</div>
  <div class="abs footer-links center" style="left:722px;top:88px">In search for staff?<br>Staff quality<br>FAQ<br>Contact us</div>

  <span class="abs social" style="left:524px;top:98px"></span>
  <span class="abs social" style="left:582px;top:98px"></span>
  <span class="abs social" style="left:638px;top:98px"></span>

  <p class="abs contact center" style="top:146px">example@email.com<br>123.456.789<br>St. Example of Street, 1025, California</p>
</footer>

<div class="abs copyright">© 2017 Copyright property of VERDANTA</div>

</body>
</html>
```